Pinecrest & Framewright Valmora Transit 3500

Need to create a wrap that really POPS. The customer is a home contractor. His website is https://pinecrestframewright.example/
He wants the wrap to capture everything he creates. The work truck is a 2012 Valmora Transit box truck 3500. The box is 12ft wide x 86" tall. The rear door is 70" tall x 70" wide. He wants to incorporate red/gray/black into the logo and design. Also, he likes the attached wrap design. Use that for inspiration, please do not copy directly.
Colors
Designer to choose colors to be used in the design.
Look and feel
Each slider illustrates characteristics of the customer's brand and the style your logo design should communicate.

```html
<!DOCTYPE html>
<html lang="en">
<head>
<meta charset="utf-8">
<title>Pinecrest &amp; Framewright – Valmora Transit 3500 side wrap</title>
<link rel="stylesheet" href="https://fonts.googleapis.com/css2?family=Archivo+Black&family=Archivo:wght@800&family=Oswald:wght@500;600&display=swap">
<style>
  :root{
    --canvas:#e9eaec;
    --wrap-white:#f4f4f4;
    --stripe-black:#141414;
    --brand-red:#4a2424;
    --ink:#111111;
    --wood-light:#8a4a3a;
    --wood-dark:#5e2e24;
    --kitchen-light:#e8e2dc;
    --kitchen-warm:#b99a84;
  }
  *{box-sizing:border-box;margin:0;padding:0}
  html,body{width:1200px;height:1200px;overflow:hidden;background:var(--canvas)}
  .canvas{position:relative;width:1200px;height:1200px}
  .wrap-side{position:absolute;left:40px;width:1120px;height:520px;background:var(--wrap-white);overflow:hidden;box-shadow:0 2px 8px rgba(0,0,0,.15)}
  .wrap-side--classic{top:50px}
  .wrap-side--kitchen{top:630px}
  .wrap-shapes{position:absolute;inset:0;width:100%;height:100%}
  .wood-band{position:absolute;left:0;right:0;top:336px;bottom:0;background:linear-gradient(180deg,var(--wood-light),var(--wood-dark))}
  .brand{position:absolute;text-align:center;color:var(--ink)}
  .brand-name{font-family:"Archivo Black",sans-serif;color:var(--brand-red);font-size:40px;letter-spacing:1px;line-height:1;white-space:nowrap}
  .brand-service{font-family:"Archivo Black",sans-serif;font-size:40px;letter-spacing:1px;line-height:1;margin-top:16px}
  .brand-scope{font-family:"Archivo",sans-serif;font-weight:800;font-size:20px;letter-spacing:1px;margin-top:12px;white-space:nowrap}
  .brand-tagline{font-family:"Oswald",sans-serif;font-weight:600;font-size:14px;line-height:1.25;margin-top:8px}
  .brand--kitchen .brand-name{font-size:28px;letter-spacing:.5px}
  .brand--kitchen .brand-service{font-size:34px;margin-top:14px}
  .brand--kitchen .brand-scope{font-size:17px;margin-top:10px}
  .stripe-text{position:absolute;color:#fff;font-family:"Oswald",sans-serif;font-weight:500;white-space:nowrap;line-height:1}
  .license{font-size:13px;letter-spacing:1px;color:#bbb}
  .phone{font-size:25px;font-weight:600;letter-spacing:2px}
  .site-small{position:absolute;font-family:"Oswald",sans-serif;font-weight:600;font-size:10px;letter-spacing:.5px;color:var(--ink)}
  .web{font-size:15px;letter-spacing:1.5px;font-weight:600}
  .tagline-stripe{font-size:13px;font-weight:600;letter-spacing:.3px}
</style>
</head>
<body>
<main class="canvas">

  <section class="wrap-side wrap-side--classic" aria-label="Side wrap, stripe layout">
    <div class="wood-band" role="img" aria-label="Reddish-brown wood plank texture band"></div>
    <svg class="wrap-shapes" viewBox="0 0 1120 520" aria-hidden="true">
      <rect x="0" y="296" width="1120" height="34" fill="var(--stripe-black)"/>
      <rect x="0" y="292" width="1120" height="2" fill="var(--stripe-black)"/>
    </svg>
    <div class="brand" style="left:340px;width:760px;top:112px">
      <div class="brand-name">PINECREST &amp; FRAMEWRIGHT</div>
      <div class="brand-service">REMODELING</div>
      <div class="brand-scope">KITCHEN | BATHROOM | HOME REPAIR</div>
    </div>
    <div class="site-small" style="left:200px;top:276px">WWW.PINECRESTFRAMEWRIGHT.EXAMPLE</div>
    <div class="stripe-text license" style="left:28px;top:306px">#LIC 00XK04417200</div>
    <div class="stripe-text phone" style="left:200px;top:300px">555 010 4821</div>
    <div class="stripe-text tagline-stripe" style="left:450px;top:306px">SPECIALIST IN WOODWORK. CUSTOM-KITCHEN. CUSTOM-BATHROOM. ADDITION AND MORE</div>
  </section>

  <section class="wrap-side wrap-side--kitchen" aria-label="Side wrap, diagonal photo layout">
    <div class="wood-band" role="img" aria-label="Reddish-brown wood plank texture band"></div>
    <svg class="wrap-shapes" viewBox="0 0 1120 520">
      <defs>
        <linearGradient id="kitchenTone" x1="0" y1="0" x2="1" y2="1">
          <stop offset="0" stop-color="var(--kitchen-light)"/>
          <stop offset="1" stop-color="var(--kitchen-warm)"/>
        </linearGradient>
      </defs>
      <path d="M880 0 H1120 V336 H720 Z" fill="url(#kitchenTone)" role="img" aria-label="Photo of a finished white custom kitchen with cabinets and island"/>
      <path d="M0 296 H700 Q730 296 742 268 L866 -4 L886 -4 L760 280 Q748 330 700 330 H0 Z" fill="var(--stripe-black)" aria-hidden="true"/>
    </svg>
    <div class="brand brand--kitchen" style="left:270px;width:520px;top:110px">
      <div class="brand-name">PINECREST &amp; FRAMEWRIGHT</div>
      <div class="brand-service">REMODELING</div>
      <div class="brand-scope">KITCHEN | BATHROOM | HOME REPAIR</div>
      <div class="brand-tagline">SPECIALIST IN WOODWORK. CUSTOM-KITCHEN. CUSTOM-BATHROOM.<br>ADDITION AND MORE</div>
    </div>
    <div class="stripe-text license" style="left:28px;top:306px">#LIC 00XK04417200</div>
    <div class="stripe-text phone" style="left:200px;top:300px">555 010 4821</div>
    <div class="stripe-text web" style="left:430px;top:305px">WWW.PINECRESTFRAMEWRIGHT.EXAMPLE</div>
  </section>

</main>
</body>
</html>
```